MT Halloway Insurance - Aviation

We are wanting to have new business cards designed for our new aviation division. We currently have business cards for the other business (attached). We would like to use the same colors and have the logo somewhere on the business card along with a small, single engine airplane, maybe in the background but would like it to be different than the original and more focused on aviation. Also wondering if there is a way to do laser cut and make the business card in the shape of an airplane? Just some different ideas that make it stand out.

Target Market(s)

Pilots

Industry/Entity Type

Insurance

Contact Information for Business Card

We would like to use the same colors and have the logo somewhere on the business card along with a small, single engine airplane, maybe in the background but would like it to be different than the original and more focused on aviation. Also wondering if there is a way to do laser cut and make the business card in the shape of an airplane? Just some different ideas that make it stand out.

Requirements
Must have
• A small, single engine airplane

```html
<!DOCTYPE html>
<html lang="en">
<head>
<meta charset="utf-8">
<title>MT Halloway Insurance – Aviation Business Card</title>
<link rel="stylesheet" href="https://fonts.googleapis.com/css2?family=Noto+Serif:wght@400;700&display=swap">
<style>
  :root {
    --backdrop: #8e8c8d;
    --brand-red: #a91c24;
    --brand-black: #121212;
    --ink-light: #f4eeee;
    --sky-light: #d6d6d6;
    --sky-mid: #9c9c9c;
    --sky-dark: #5a5a5a;
  }
  * { margin: 0; padding: 0; box-sizing: border-box; }
  html, body {
    width: 1200px;
    height: 1101px;
    overflow: hidden;
    background: var(--backdrop);
    font-family: "Noto Serif", Georgia, serif;
  }
  .canvas { position: relative; width: 1200px; height: 1101px; }
  .card {
    position: absolute;
    top: 277px;
    width: 303px;
    height: 511px;
    overflow: hidden;
    color: var(--ink-light);
  }
  .card--front { left: 246px; background: var(--brand-red); }
  .card--back { left: 641px; background: var(--brand-red); }

  .agent {
    position: absolute;
    right: 36px;
    top: 44px;
    text-align: right;
  }
  .agent__name {
    font-weight: 700;
    font-size: 33px;
    line-height: 40px;
    letter-spacing: 1px;
    text-transform: uppercase;
  }
  .agent__title {
    margin-top: 10px;
    font-size: 17.5px;
    letter-spacing: 0.4px;
  }
  .contact {
    position: absolute;
    left: 35px;
    top: 289px;
    font-size: 17px;
    line-height: 23px;
    letter-spacing: 0.3px;
  }
  .contact__group + .contact__group { margin-top: 22px; }
  .contact__rule {
    position: absolute;
    left: 252px;
    top: 291px;
    width: 2px;
    height: 184px;
    background: var(--ink-light);
  }

  .back__base {
    position: absolute;
    left: 0; top: 269px;
    width: 100%; height: 242px;
    background: var(--brand-black);
  }
  .back__photo { position: absolute; left: 0; top: 0; }
  .brand-name {
    position: absolute;
    left: 0; right: 0;
    top: 446px;
    text-align: center;
    font-size: 16.5px;
    letter-spacing: 0.3px;
    text-transform: uppercase;
    color: var(--ink-light);
  }
</style>
</head>
<body>
<main class="canvas">
  <section class="card card--front">
    <div class="agent">
      <h1 class="agent__name">Daniel<br>Halloway</h1>
      <p class="agent__title">Principal Agent</p>
    </div>
    <div class="contact">
      <p class="contact__group">555 214 3370<br>daniel@mthins.com</p>
      <p class="contact__group">Cell: 555 318 6042<br>www.mthins.com</p>
      <p class="contact__group">512 Meadow Parkway<br>Alden, Texas 76010</p>
    </div>
    <span class="contact__rule"></span>
  </section>

  <section class="card card--back">
    <div class="back__base"></div>
    <svg class="back__photo" width="303" height="511" viewBox="0 0 303 511" role="img" aria-label="Photo of an airliner climbing overhead against a cloudy sky, cut out along the aircraft outline">
      <defs>
        <linearGradient id="sky-fill" x1="0" y1="0" x2="1" y2="1">
          <stop offset="0" stop-color="var(--sky-light)"/>
          <stop offset="0.55" stop-color="var(--sky-mid)"/>
          <stop offset="1" stop-color="var(--sky-dark)"/>
        </linearGradient>
      </defs>
      <path d="M0,58 L96,36 Q112,32 120,44 L196,150 Q204,160 220,160 L303,174 L303,334 L120,344 Q108,344 104,332 L92,269 L0,269 Z" fill="url(#sky-fill)"/>
    </svg>
    <p class="brand-name">MT Halloway Insurance</p>
  </section>
</main>
</body>
</html>
```